Brennick Setter Club - Rare dog breed club needs web design!

The Transylvanian Hound (or Erdélyi kopó) is an ancient Hungarian dog breed. These medium-sized hounds were favored by the Hungarian kings and princes for hunting bears and wolves in the Carpathian mountains of Transylvania. The breed's great adaptability to the region's extreme climates of sweltering summers and frigid winters made it an excellent all season hunting dog. This dog has a sleek appearance and stunning good looks. They are lean, appear very elegant and proud. Their erect posture and beautifully sculpted head portray great attentiveness and authority. In general, this rare breed is extremely good natured, loyal and obedient. It has a tendency to form strong attachments to its primary caretakers and will remain loyal and protective. (Please refer to existing web resources.)

The Brennick Setter Club - with current website www.brennicksetter.com - is the official breed club of Transylvanian Hound afficionados, breeders and owners in the United States, which was founded in 2010. We are looking for a web design for the new, upgraded version of this central (currenty non-functioning) website. Please do not recycle the old logo (we may choose from your suggesions and pay for it!) or any of the old texts. Please use the structure described below. Overall, the webpage serves a dual purpose: an educational one (about the breed itself) and a community-building one (inside the Club). The proposed structure of the website is as follows:

1. About the Kopó
- Breed History
- Breed Standard
- Public Education
- Photo Gallery

2. Life with a Kopó
- Health and Genetics
- Feeding and Nutrition
- Training and Activities

3. Finding a Kopó
- Is this the Right Breed for You?
- Choosing a Puppy
- FAQ
- Breeder Referral

4. The Brennick Setter Club
- Constituton
- Officers and Appointees
- Code of Ethics
- Breeder Guidelines
- Membership
- Reports
- Links

5. News and Events

6. Shop

We are attaching a couple of examples of the graphics/drawings of the dogs that would be part of the design of the website. We plan to have more of these artistic depictions, nicely embedded into the background (maybe shaded out at the edges just like the drawings themselves) and less actual photos. Or a good combination of the two.

Further information upon request.

Reason: There are a few very promising design collaborations ongoing. As we moved the brief to a more artistic and graphic direction, we felt that one week of extension would be needed to get to the perfect end-product, which could include designs for sub-pages as well.

Reason: In order to make the final modifications to the leading designs, and at the request of those designers, the deadline is extended until Friday.

Target Market(s)

- BRSC Club members, dog (especially T-Hound) owners, past and future owners, breeders, puppy buyers, hunters, kennel clubs, dog show participants, vets, animal shelters, Hungarian, Romanian and other European web visitors, historians

Industry/Entity Type

Club

Font styles to use
Serif
Decorative
Script

Requirements
Must have
• - Sync with graphics of dogs (see attachments), but accentuate the rich black basic color of the dogs
- Elegance, aristocratic/noble look and feel (but not overly archaic)
- Love, companionship, dogs as family members
- Hunting usage, but no bloody associations, rather romantic ones
- Simple to use and navigate for non-web-natives
- Old world (Central European) atmosphere, even the exotic, rustic and romantic Transylvanian feel - SEE the new attachment for inspiration (this was a design plan which we discarded (mainly because of its gothic, (nazi-like), unreadable font, and the fact that the plan makes the black-looking dogs appear brown), however we loved the fact that it was not full of boxes/windows, had a marble/sand stone like continuous background, lots of little elegant graphics, the drawings embedded, etc.
Nice to have
• - Working on smartphone, Zentabs, etc., so dynamic website design
- Web shop to be added to functionalities in the future (?)
- English language for now, in the future can be Hungarian, Romanian, etc., so the font choice should handle various alphabets
- Focus on the dogs (likely more graphics than photos, at least on the main pages), and not on the activities/humans - the design should accentuate the black and not the tan of the graphics!
Should not have
• - Old logo from the old www.brennicksetter.com webpage or the other logo from the Chatterly site of the Brennick Setter Club, we will have a new one (maybe designed by you!)
- Breed club, kennel club cliches
- Cutesy, adorable, cheesy design elements
- Old, stale, monolithic, archaic, snobbish, etc. look and feel
- No vampire associations

```html
<!DOCTYPE html>
<html lang="en">
<head>
<meta charset="utf-8">
<title>Brennick Setter Club</title>
<link rel="stylesheet" href="https://fonts.googleapis.com/css2?family=Cinzel:wght@400;600&family=Arimo:wght@400&display=swap">
<style>
:root{
  --sand:#e4d5b4;
  --sand-light:#e9dcbd;
  --ink:#2a2620;
  --rust:#b8561c;
  --link:#2b55a3;
  --rule:#ad9c79;
  --muted:#5a5249;
  --sketch-dark:#5c5448;
  --sketch-mid:#a08a6a;
  --sketch-light:#d9c9a8;
}
*{margin:0;padding:0;box-sizing:border-box}
html,body{width:1200px;height:1029px;overflow:hidden}
body{
  position:relative;
  background:radial-gradient(ellipse at 50% 40%,var(--sand-light),var(--sand) 70%);
  font-family:"Arimo",Arial,sans-serif;
  color:var(--ink);
}
.abs{position:absolute}
.caps{font-family:"Cinzel",serif;font-variant:small-caps;text-transform:none}
.brand{left:233px;top:34px;width:340px;font-family:"Cinzel",serif;font-weight:400;font-size:38px;line-height:44px;color:var(--rust)}
.utility-nav{left:780px;top:49px;width:180px;display:flex;justify-content:flex-end;gap:17px;font-size:13px;letter-spacing:.3px}
.utility-nav a,.main-nav a{color:var(--ink);text-decoration:none}
.rule{height:0;border-top:1px dashed var(--rule)}
.main-nav{left:225px;top:146px;width:750px;height:40px;display:flex;justify-content:space-between;align-items:center;padding:0 16px 0 17px;font-size:16px;letter-spacing:.3px}
.main-nav a.current{color:var(--rust)}
.sketch{background:radial-gradient(ellipse at 50% 50%,var(--sketch-dark) 0%,var(--sketch-mid) 40%,var(--sketch-light) 65%,rgba(228,213,180,0) 75%)}
.section-title{font-family:"Cinzel",serif;font-weight:600;color:var(--rust);font-size:24px;letter-spacing:.4px}
.copy{font-size:11px;line-height:18.9px;color:#3a352e}
.more{font-family:"Cinzel",serif;font-weight:600;font-size:13.5px;color:var(--link);text-decoration:none}
.gallery-title{left:284px;top:500px;font-size:22px;line-height:25px}
.thumb{top:492px;width:123px;height:77px;background:linear-gradient(100deg,#c9bea6 0%,#c2b49a 35%,#7a5a3e 60%,#4a3a2c 85%,#c4b9a1 100%)}
.footer-text{left:0;top:962px;width:1200px;text-align:center;font-size:10.5px;color:var(--muted);letter-spacing:.2px}
.footer-text span{margin-left:12px}
</style>
</head>
<body>
  <div class="abs brand">Brennick Setter Club</div>

  <nav class="abs utility-nav caps"><a href="#">News and Events</a><a href="#">Shop</a></nav>

  <div class="abs rule" style="left:225px;top:146px;width:750px"></div>
  <nav class="abs main-nav caps">
    <a class="current" href="#">About the Kopó</a>
    <a href="#">Life with a Kopó</a>
    <a href="#">Finding a Kopó</a>
    <a href="#">The Brennick Setter Club</a>
  </nav>
  <div class="abs rule" style="left:225px;top:186px;width:750px"></div>

  <div class="abs sketch" role="img" aria-label="Pencil drawing of a black and tan hound licking its nose" style="left:210px;top:219px;width:326px;height:231px"></div>

  <h2 class="abs section-title caps" style="left:576px;top:223px">About the Kopó</h2>
  <p class="abs copy" style="left:575px;top:260px;width:392px">Lorem ipsum dolor sit amet, consectetuer adipiscing elit, sed diam nonummy nibh euismod tincidunt ut laoreet dolore magna aliquam erat volutpat. Ut wisi enim ad minim veniam, quis nostrud exerci tation ullamcorper suscipit lobortis nisl ut aliquip ex ea commodo consequat. Duis autem vel eum iriure dolor in hendrerit in vulputate velit esse molestie consequat, vel illum dolore eu feugiat nulla facilisis at vero eros et accumsan et iusto odio dignissim qui blandit praesent luptatum zzril delenit augue duis dolore te feugait nulla facilisi. Nam liber tempor cum soluta nobis eleifend.</p>
  <a class="abs more caps" href="#" style="left:573px;top:420px">Learn more</a>

  <div class="abs rule" style="left:225px;top:469px;width:750px"></div>

  <h2 class="abs section-title caps gallery-title">Photo<br>Gallery</h2>
  <div class="abs thumb" role="img" aria-label="Gallery photo of a hound in profile" style="left:399px"></div>
  <div class="abs thumb" role="img" aria-label="Gallery photo of a hound in profile" style="left:536px"></div>
  <div class="abs thumb" role="img" aria-label="Gallery photo of a hound in profile" style="left:673px"></div>
  <div class="abs thumb" role="img" aria-label="Gallery photo of a hound in profile" style="left:810px"></div>

  <div class="abs rule" style="left:225px;top:589px;width:750px"></div>

  <h2 class="abs section-title caps" style="left:240px;top:634px">The Brennick Setter Club</h2>
  <p class="abs copy" style="left:249px;top:673px;width:392px">Lorem ipsum dolor sit amet, consectetuer adipiscing elit, sed diam nonummy nibh euismod tincidunt ut laoreet dolore magna aliquam erat volutpat. Ut wisi enim ad minim veniam, quis nostrud exerci tation ullamcorper suscipit lobortis nisl ut aliquip ex ea commodo consequat. Duis autem vel eum iriure dolor in hendrerit in vulputate velit esse molestie consequat, vel illum dolore eu feugiat nulla facilisis at vero eros et accumsan et iusto odio dignissim qui blandit praesent luptatum zzril delenit augue duis dolore te feugait nulla facilisi. Nam liber tempor cum soluta nobis eleifend.</p>
  <a class="abs more caps" href="#" style="left:252px;top:834px">Learn more</a>

  <div class="abs sketch" role="img" aria-label="Pencil drawing of two black and tan hounds looking upward" style="left:714px;top:620px;width:230px;height:295px"></div>

  <div class="abs rule" style="left:0;top:943px;width:1200px"></div>
  <footer class="abs footer-text">Copyright 2014 The Brennick Setter Club <span>Terms &amp; Conditions | Privacy Policy</span></footer>
</body>
</html>
```